Environmental Consultancy needs new professional Word Template for reporting

A professional looking word template that we can use for all of our reporting.

Word template needs:
- a full scale title page that we can include a different photograph on for each new project, our company logo, title, date, and client details
- Include four layered Headings, table of contents page.
- Each page (except title page) needs to be numbered, with the title of the report at the bottom of the page.
- each page needs our company logo at the top.
- Prefer it to be using similar colours to what we are currently using. Though open to new colours if you come up with something that suits what we do.

Our business is an environment/ecological consultancy and we provide a number of field and reporting based services to mining companies, government agencies, commercial developers, landholders, tourism operators etc. Some of the work we do includes:
- vegetation surveys and reporting
- fauna trapping surveys, and reporting
- water quality and aquatic ecosystem monitoring and reporting
- fish and macroinvertebrate surveys
- seagrass and coral surveys
- environmental impact statements
- environmental offsets
- rehabilitation design and monitoring
- monitoring design programs
- ecological constraints surveys.

I have attached our company logo, a copy of our current title page, and an extract of our current report style (has been greatly reduced and with client information removed). I would like sometime similar to this report style please.

Target Market(s)

Client and Government approval agencies

Industry/Entity Type

Environmental Consultant

Font styles to use
Sans Serif

Colors
faa54b
9bcb3c
00a990
83c9e6
85acd3

Requirements
Must have
• Word template needs:

```html
<!DOCTYPE html>
<html lang="en">
<head>
<meta charset="utf-8">
<title>Report Template – Field Results Report</title>
<link href="https://fonts.googleapis.com/css2?family=Montserrat:wght@400;500;600;700;800&family=Oswald:wght@600&display=swap" rel="stylesheet">
<style>
:root{
  --ink:#4a4a4a;
  --muted:#8a8a8a;
  --rust:#c0733a;
  --gold:#d5a04c;
  --teal:#1f7f78;
  --peach:#fbe7d8;
  --tan:#c99a6b;
  --stage-dark:#2b2b2b;
  --stage-light:#ececec;
  --paper:#ffffff;
  --forest:#4f6b4c;
  --mist:#b9c2b5;
}
*{box-sizing:border-box;margin:0;padding:0}
html,body{width:1200px;height:4246px;overflow:hidden}
body{font-family:'Montserrat',sans-serif;color:var(--ink);background:var(--stage-light);position:relative}
.stage-top{position:absolute;left:0;top:0;width:1200px;height:900px;background:var(--stage-dark)}
.hero-cover{position:absolute;left:381px;top:129px;transform:scale(.847);transform-origin:0 0;box-shadow:0 14px 40px rgba(0,0,0,.45)}
.section-label{position:absolute;top:930px;left:0;width:1200px;text-align:center;font-family:'Oswald',sans-serif;font-weight:600;font-size:118px;letter-spacing:4px;color:#c9c9c9;line-height:1}

.page{position:absolute;width:517px;height:743px;background:var(--paper);overflow:hidden;box-shadow:0 4px 12px rgba(0,0,0,.12)}
.page.peach{background:var(--peach)}
.col-l{left:63px}.col-r{left:621px}
.row-1{top:1091px}.row-2{top:1880px}.row-3{top:2670px}.row-4{top:3458px}

.cover-art{position:absolute;inset:0;width:100%;height:100%}
.cover-title{position:absolute;left:58px;top:440px;font-weight:800;font-size:23px;line-height:1.2;color:var(--gold);letter-spacing:.3px}
.cover-sub{position:absolute;left:58px;top:545px;font-weight:500;font-size:16px;color:var(--gold);letter-spacing:.4px}
.cover-prepared{position:absolute;left:58px;top:604px;font-size:12.5px;line-height:1.45;color:var(--muted)}
.cover-logo{position:absolute;right:24px;bottom:26px}

.brand{display:flex;align-items:center;gap:5px;font-weight:600;color:var(--gold);white-space:nowrap}
.brand .dot{border-radius:50%;background:var(--teal);flex:none}
.brand.lg{font-size:24px}.brand.lg .dot{width:12px;height:12px}
.brand.sm{font-size:12px}.brand.sm .dot{width:6px;height:6px}
.page-logo{position:absolute;top:22px;right:30px}

.page-body{position:absolute;left:52px;right:52px;top:62px;bottom:40px}
h1.section{font-weight:800;font-size:25px;color:var(--rust);letter-spacing:.3px;margin-bottom:34px}
h2.sub{font-weight:700;font-size:8px;color:var(--rust);margin:12px 0 7px}
h3.minor{font-weight:600;font-size:6px;color:var(--ink);margin:6px 0 5px}
p.body{font-size:4.8px;line-height:1.5;text-align:justify;margin-bottom:6px;color:#555}
.peach p.body{margin-bottom:9px}
.exec h1.section{margin-bottom:60px}

.page-foot{position:absolute;left:52px;right:52px;bottom:14px;border-top:1px solid #e3c7ad;padding-top:5px;display:flex;justify-content:space-between;font-size:5px;font-weight:600;color:var(--rust);letter-spacing:.3px}

.photo{position:absolute;display:block}
.photo-river{left:0;top:124px;width:168px;height:570px;background:linear-gradient(180deg,#1f2a25 0%,#3b5a4f 35%,#5f8f8c 55%,#6b4d36 80%,#2c2620 100%)}
.photo-stream{right:36px;top:124px;width:138px;height:150px;background:linear-gradient(160deg,#3f6a35 0%,#6f9550 40%,#b8c8c0 65%,#4d5a44 100%)}
.text-beside-left{position:absolute;left:188px;right:36px;top:124px}
.text-beside-right{position:absolute;left:52px;right:190px;top:124px}
.text-below{position:absolute;left:52px;right:36px;top:290px}

table.data{width:100%;border-collapse:collapse;font-size:5px;margin-bottom:26px}
table.data th{background:var(--tan);color:#fff;font-weight:600;text-align:left;padding:3px 4px}
table.data td{padding:3px 4px;border-bottom:1px solid #ececec;color:#555}
table.data tr.hl td{color:var(--rust);background:#fbeee3}

.charts{display:flex;justify-content:space-between;margin-top:-6px}
.charts svg{width:196px;height:186px}
.chart-text{font-family:'Montserrat',sans-serif;font-size:6px;fill:#666}

.contact{position:absolute;left:52px;top:500px;font-size:7px;color:#555}
.contact li{list-style:none;display:flex;gap:12px;margin-bottom:16px;line-height:1.45}
.contact svg{width:14px;height:12px;flex:none;margin-top:1px}
</style>
</head>
<body>

<div class="stage-top"></div>

<!-- Front cover, featured -->
<div class="page hero-cover">
  <svg class="cover-art" viewBox="0 0 100 144" preserveAspectRatio="none" aria-hidden="true">
    <defs>
      <linearGradient id="forestA" x1="0" y1="0" x2="0.6" y2="1">
        <stop offset="0" stop-color="#a9b5a4"/><stop offset=".4" stop-color="#4f6b4c"/><stop offset=".75" stop-color="#7e9a77"/><stop offset="1" stop-color="#d8dcd4"/>
      </linearGradient>
      <linearGradient id="baseA" x1="0" y1="0" x2="1" y2="0">
        <stop offset="0" stop-color="#1f7f78"/><stop offset=".6" stop-color="#6fb1a8"/><stop offset="1" stop-color="#d5a04c"/>
      </linearGradient>
    </defs>
    <rect width="100" height="144" fill="url(#forestA)" role="img" aria-label="Project photograph: rainforest with waterfall"/>
    <path d="M0,50 C35,52 70,68 100,84 L100,89 C70,73 35,57 0,54 Z" fill="#d5a04c"/>
    <path d="M0,54 C35,57 70,73 100,89 L100,101 C74,86 40,65 0,58 Z" fill="#1f7f78"/>
    <path d="M0,58 C40,65 74,86 100,101 L100,144 L0,144 Z" fill="#fff"/>
    <path d="M0,137 C35,132 70,140 100,130 L100,144 L0,144 Z" fill="url(#baseA)" opacity=".85"/>
  </svg>
  <div class="cover-title">RECEIVING<br>ENVIRONMENT<br>MONITORING PROGRAM</div>
  <div class="cover-sub">FIELD RESULTS REPORT</div>
  <div class="cover-prepared">Prepared on behalf of (insert client name)<br>August 2020</div>
  <div class="cover-logo"><div class="brand lg"><span class="dot"></span>Canopy Ecology</div></div>
</div>

<div class="section-label">PAGES</div>

<!-- Page: front cover -->
<div class="page col-l row-1">
  <svg class="cover-art" viewBox="0 0 100 144" preserveAspectRatio="none" aria-hidden="true">
    <defs>
      <linearGradient id="forestB" x1="0" y1="0" x2="0.6" y2="1">
        <stop offset="0" stop-color="#a9b5a4"/><stop offset=".4" stop-color="#4f6b4c"/><stop offset=".75" stop-color="#7e9a77"/><stop offset="1" stop-color="#d8dcd4"/>
      </linearGradient>
      <linearGradient id="baseB" x1="0" y1="0" x2="1" y2="0">
        <stop offset="0" stop-color="#1f7f78"/><stop offset=".6" stop-color="#6fb1a8"/><stop offset="1" stop-color="#d5a04c"/>
      </linearGradient>
    </defs>
    <rect width="100" height="144" fill="url(#forestB)" role="img" aria-label="Project photograph: rainforest with waterfall"/>
    <path d="M0,50 C35,52 70,68 100,84 L100,89 C70,73 35,57 0,54 Z" fill="#d5a04c"/>
    <path d="M0,54 C35,57 70,73 100,89 L100,101 C74,86 40,65 0,58 Z" fill="#1f7f78"/>
    <path d="M0,58 C40,65 74,86 100,101 L100,144 L0,144 Z" fill="#fff"/>
    <path d="M0,137 C35,132 70,140 100,130 L100,144 L0,144 Z" fill="url(#baseB)" opacity=".85"/>
  </svg>
  <div class="cover-title">RECEIVING<br>ENVIRONMENT<br>MONITORING PROGRAM</div>
  <div class="cover-sub">FIELD RESULTS REPORT</div>
  <div class="cover-prepared">Prepared on behalf of (insert client name)<br>August 2020</div>
  <div class="cover-logo"><div class="brand lg"><span class="dot"></span>Canopy Ecology</div></div>
</div>

<!-- Page: executive summary -->
<div class="page peach exec col-r row-1">
  <div class="page-logo"><div class="brand sm"><span class="dot"></span>Canopy Ecology</div></div>
  <div class="page-body">
    <h1 class="section">EXECUTIVE SUMMARY</h1>
    <p class="body">This report presents the results of an environmental assessment for The Ridges residential development on Lot 1 in Brisbane, Queensland. The proponent plans to add residential lots to an approved stage, and an application for reconfiguring a lot is required.</p>
    <p class="body">The assessment involved a desktop review of environmental values and a field survey to ground-truth those values using best practice methods. The findings were assessed against the relevant overlay codes of the City Plan and State Code 16.</p>
    <p class="body">The field survey confirmed that the mapped regional ecosystems were broadly accurate, with only slight changes to boundaries. Remnant vegetation present within the development area is of least concern status, and narrow strips of non-remnant vegetation occur to the north and east.</p>
    <p class="body">No threatened flora or fauna were observed during the field survey. Some threatened species may occur given the location and soil types present, however the low ecological function of the vegetation means use of the area is expected to be minimal.</p>
    <p class="body">While the condition of the remnant vegetation is good, its ecological function is low due to edge effects and ongoing disturbance from surrounding urban land uses. The vegetation provides some habitat for common species tolerant of disturbed environments.</p>
    <p class="body">Based on these results, impacts from the proposed development will be low. Clearing has been kept to non-remnant areas where possible, and a set of recommendations has been provided to guide construction and protect environmental values.</p>
    <p class="body">To compensate for clearing, the developers have set aside land as a nature refuge adjoining the development, providing an ecological corridor along the waterway to the west.</p>
    <p class="body">Assessment against the Natural Assets Overlay Code and State Code 16 confirms that the proposed development is compliant with all relevant performance outcomes.</p>
  </div>
  <div class="page-foot"><span>RECEIVING ENVIRONMENT MONITORING PROGRAM – FIELD RESULTS REPORT</span><span>2</span></div>
</div>

<!-- Page: introduction -->
<div class="page col-l row-2">
  <div class="page-logo"><div class="brand sm"><span class="dot"></span>Canopy Ecology</div></div>
  <div class="page-body">
    <h1 class="section">1. INTRODUCTION</h1>
    <h2 class="sub">1.1 BACKGROUND</h2>
    <p class="body">Canopy Ecology has been engaged by (insert client name) to undertake an environmental assessment of their residential development site, The Ridges, located in Brisbane, Queensland.</p>
    <p class="body">The client is required to prepare a development application for reconfiguring a lot to allow an increase in the number of residential lots they have already approved at The Ridges.</p>
    <p class="body">Construction of the new lots will require clearing of native vegetation that is mapped as remnant vegetation and as an area of high environmental importance under the City Plan.</p>
    <p class="body">This assessment report has been prepared to provide a response to the Natural Assets Overlay Code and State Code 16, and will accompany the development application.</p>
    <h2 class="sub">1.2 DEVELOPMENT PLANS</h2>
    <p class="body">The Ridges development is a large scale residential housing estate. Much of the estate has been planned and approved, with the first few stages already under construction.</p>
    <p class="body">The proposed new lots and associated infrastructure cover an area of approximately 4.4 hectares, referred to as the development area within the rest of this report.</p>
    <h2 class="sub">1.3 SITE DESCRIPTION AND ENVIRONMENTAL SETTING</h2>
    <p class="body">The site is situated in the Plains subregion of the Southeast Queensland bioregion. The region typically experiences warm wet summers and dry winters, with most rain falling between November and April.</p>
    <p class="body">One waterway, a stream order 2, runs through the development area, flowing from south to north before joining the larger river downstream of the site.</p>
  </div>
  <div class="page-foot"><span>RECEIVING ENVIRONMENT MONITORING PROGRAM – FIELD RESULTS REPORT</span><span>3</span></div>
</div>

<!-- Page: headings -->
<div class="page col-r row-2">
  <div class="page-logo"><div class="brand sm"><span class="dot"></span>Canopy Ecology</div></div>
  <div class="page-body">
    <h1 class="section">2. LOREM IPSUM</h1>
    <h2 class="sub">2.1 LOREM IPSUM</h2>
    <h3 class="minor">2.1.1 Lorem ipsum dolor sit amet</h3>
    <p class="body">Sample body text shows how paragraphs sit within the template. Each section follows the same spacing, margins and type sizes, so reports stay consistent across projects. Replace this copy with survey findings, methods, results and discussion for the relevant site. Sample body text shows how paragraphs sit within the template and how longer sections wrap across several lines of justified copy.</p>
    <p class="body">Sample body text shows how paragraphs sit within the template. Each section follows the same spacing, margins and type sizes, so reports stay consistent across projects. Replace this copy with survey findings, methods, results and discussion for the relevant site.</p>
    <p class="body">Sample body text shows how paragraphs sit within the template. Each section follows the same spacing, margins and type sizes, so reports stay consistent across projects. Replace this copy with survey findings, methods, results and discussion for the relevant site.</p>
    <h3 class="minor">2.1.2 Lorem ipsum dolor sit amet</h3>
    <p class="body">Sample body text shows how paragraphs sit within the template. Each section follows the same spacing, margins and type sizes, so reports stay consistent across projects. Replace this copy with survey findings, methods, results and discussion for the relevant site. Sample body text shows how paragraphs sit within the template and how longer sections wrap across several lines of justified copy.</p>
    <p class="body">Sample body text shows how paragraphs sit within the template. Each section follows the same spacing, margins and type sizes, so reports stay consistent across projects. Replace this copy with survey findings, methods, results and discussion for the relevant site.</p>
    <p class="body">Sample body text shows how paragraphs sit within the template. Each section follows the same spacing, margins and type sizes, so reports stay consistent across projects. Replace this copy with survey findings, methods, results and discussion for the relevant site.</p>
  </div>
  <div class="page-foot"><span>RECEIVING ENVIRONMENT MONITORING PROGRAM – FIELD RESULTS REPORT</span><span>4</span></div>
</div>

<!-- Page: text with tall image -->
<div class="page col-l row-3">
  <div class="page-logo"><div class="brand sm"><span class="dot"></span>Canopy Ecology</div></div>
  <div class="page-body"><h1 class="section">3. TEXT WITH IMAGES</h1></div>
  <div class="photo photo-river" role="img" aria-label="Photograph: rocky creek flowing through forest"></div>
  <div class="text-beside-left">
    <p class="body">Sample body text shows how paragraphs sit within the template. Each section follows the same spacing, margins and type sizes, so reports stay consistent across projects. Replace this copy with survey findings, methods, results and discussion for the relevant site. Sample body text shows how paragraphs sit within the template and how longer sections wrap across several lines of justified copy.</p>
    <p class="body">Sample body text shows how paragraphs sit within the template. Each section follows the same spacing, margins and type sizes, so reports stay consistent across projects. Replace this copy with survey findings, methods, results and discussion for the relevant site.</p>
    <p class="body">Sample body text shows how paragraphs sit within the template. Each section follows the same spacing, margins and type sizes, so reports stay consistent across projects. Replace this copy with survey findings, methods, results and discussion for the relevant site. Sample body text shows how paragraphs sit within the template and how longer sections wrap across several lines of justified copy.</p>
    <p class="body">Sample body text shows how paragraphs sit within the template. Each section follows the same spacing, margins and type sizes, so reports stay consistent across projects. Replace this copy with survey findings, methods, results and discussion for the relevant site. Sample body text shows how paragraphs sit within the template and how longer sections wrap across several lines of justified copy.</p>
  </div>
  <div class="page-foot"><span>RECEIVING ENVIRONMENT MONITORING PROGRAM – FIELD RESULTS REPORT</span><span>5</span></div>
</div>

<!-- Page: text with inset image -->
<div class="page col-r row-3">
  <div class="page-logo"><div class="brand sm"><span class="dot"></span>Canopy Ecology</div></div>
  <div class="page-body"><h1 class="section">4. TEXT WITH IMAGES</h1></div>
  <div class="photo photo-stream" role="img" aria-label="Photograph: forest stream over rocks"></div>
  <div class="text-beside-right">
    <p class="body">Sample body text shows how paragraphs sit within the template. Each section follows the same spacing, margins and type sizes, so reports stay consistent across projects. Replace this copy with survey findings, methods, results and discussion for the relevant site. Sample body text shows how paragraphs sit within the template and how longer sections wrap across several lines of justified copy.</p>
  </div>
  <div class="text-below">
    <p class="body">Sample body text shows how paragraphs sit within the template. Each section follows the same spacing, margins and type sizes, so reports stay consistent across projects. Replace this copy with survey findings, methods, results and discussion for the relevant site.</p>
    <p class="body">Sample body text shows how paragraphs sit within the template. Each section follows the same spacing, margins and type sizes, so reports stay consistent across projects. Replace this copy with survey findings, methods, results and discussion for the relevant site.</p>
    <h2 class="sub">2.1 LOREM IPSUM</h2>
    <h3 class="minor">2.1.1 Lorem ipsum dolor sit amet</h3>
    <p class="body">Sample body text shows how paragraphs sit within the template. Each section follows the same spacing, margins and type sizes, so reports stay consistent across projects. Replace this copy with survey findings, methods, results and discussion for the relevant site. Sample body text shows how paragraphs sit within the template and how longer sections wrap across several lines of justified copy.</p>
    <p class="body">Sample body text shows how paragraphs sit within the template. Each section follows the same spacing, margins and type sizes, so reports stay consistent across projects. Replace this copy with survey findings, methods, results and discussion for the relevant site.</p>
  </div>
  <div class="page-foot"><span>RECEIVING ENVIRONMENT MONITORING PROGRAM – FIELD RESULTS REPORT</span><span>6</span></div>
</div>

<!-- Page: tables and charts -->
<div class="page col-l row-4">
  <div class="page-logo"><div class="brand sm"><span class="dot"></span>Canopy Ecology</div></div>
  <div class="page-body">
    <h1 class="section">5. TABLES</h1>
    <table class="data">
      <tr><th>Section</th><th>Tabular Column</th><th></th><th>Company</th><th>Reference</th><th>Page(s)</th></tr>
      <tr><td>1.0</td><td>Reference 1</td><td>Header 1</td><td>Canopy Ecology</td><td>2.0</td><td>1-8</td></tr>
      <tr><td>2.0</td><td>Reference 2</td><td>Header 2</td><td>Canopy Ecology</td><td>2.0, 2.1</td><td>8, 9,10</td></tr>
      <tr><td>3.0</td><td>Reference 3</td><td>Header 3</td><td>Company A</td><td>3.0, 3.1</td><td>10,11,12</td></tr>
      <tr><td>4.0</td><td>Reference 4</td><td>Header 4</td><td>Company A</td><td>2.0, 3.0A4</td><td>12,13,14</td></tr>
      <tr><td>5.0</td><td>Reference 5</td><td>Header 5</td><td>Company B</td><td>3.0</td><td>14,15</td></tr>
    </table>
    <table class="data">
      <tr><th>Section</th><th>Tabular Column</th><th></th><th>Company</th><th>Reference</th><th>Page(s)</th></tr>
      <tr><td>1.0</td><td>Reference 1</td><td>Header 1</td><td>Canopy Ecology</td><td>2.0</td><td>1-8</td></tr>
      <tr class="hl"><td>2.0</td><td>Reference 2</td><td>Header 2</td><td>Canopy Ecology</td><td>2.0, 2.1</td><td>8, 9,10</td></tr>
      <tr><td>3.0</td><td>Reference 3</td><td>Header 3</td><td>Company A</td><td>3.0, 3.1</td><td>10,11,12</td></tr>
      <tr><td>4.0</td><td>Reference 4</td><td>Header 4</td><td>Company A</td><td>2.0, 3.0A4</td><td>12,13,14</td></tr>
      <tr><td>5.0</td><td>Reference 5</td><td>Header 5</td><td>Company B</td><td>3.0</td><td>14,15</td></tr>
    </table>
    <h1 class="section" style="margin-bottom:14px">6. CHARTS</h1>
    <div class="charts">
      <svg viewBox="0 0 196 186" aria-label="Bar chart of three series across four categories">
        <g class="chart-text">
          <text x="2" y="12">6</text><text x="2" y="38">5</text><text x="2" y="64">4</text><text x="2" y="90">3</text><text x="2" y="116">2</text><text x="2" y="142">1</text><text x="2" y="168">0</text>
        </g>
        <line x1="14" y1="166" x2="194" y2="166" stroke="#ccc" stroke-width=".6"/>
        <g fill="#b5773f"><rect x="24" y="55" width="5" height="111"/><rect x="69" y="101" width="5" height="65"/><rect x="114" y="75" width="5" height="91"/><rect x="159" y="49" width="5" height="117"/></g>
        <g fill="#d8b38a"><rect x="30" y="103" width="5" height="63"/><rect x="75" y="52" width="5" height="114"/><rect x="120" y="120" width="5" height="46"/><rect x="165" y="120" width="5" height="46"/></g>
        <g fill="#ecd6bf"><rect x="36" y="114" width="5" height="52"/><rect x="81" y="114" width="5" height="52"/><rect x="126" y="88" width="5" height="78"/><rect x="171" y="36" width="5" height="130"/></g>
        <g class="chart-text"><text x="18" y="176">Category 1</text><text x="63" y="176">Category 2</text><text x="108" y="176">Category 3</text><text x="153" y="176">Category 4</text>
        <rect x="34" y="181" width="5" height="3" fill="#b5773f"/><text x="41" y="184">Series 1</text>
        <rect x="76" y="181" width="5" height="3" fill="#d8b38a"/><text x="83" y="184">Series 2</text>
        <rect x="118" y="181" width="5" height="3" fill="#ecd6bf"/><text x="125" y="184">Series 3</text></g>
      </svg>
      <svg viewBox="0 0 196 186" aria-label="Line chart of three series across four categories">
        <g class="chart-text">
          <text x="2" y="12">6</text><text x="2" y="38">5</text><text x="2" y="64">4</text><text x="2" y="90">3</text><text x="2" y="116">2</text><text x="2" y="142">1</text><text x="2" y="168">0</text>
        </g>
        <line x1="14" y1="166" x2="194" y2="166" stroke="#ccc" stroke-width=".6"/>
        <polyline points="30,55 75,101 120,75 165,49" fill="none" stroke="#b5773f" stroke-width="1.2"/>
        <polyline points="30,103 75,52 120,120 165,120" fill="none" stroke="#d8b38a" stroke-width="1.2"/>
        <polyline points="30,114 75,114 120,88 165,36" fill="none" stroke="#ecd6bf" stroke-width="1.2"/>
        <g class="chart-text"><text x="18" y="176">Category 1</text><text x="63" y="176">Category 2</text><text x="108" y="176">Category 3</text><text x="153" y="176">Category 4</text>
        <rect x="34" y="181" width="5" height="3" fill="#b5773f"/><text x="41" y="184">Series 1</text>
        <rect x="76" y="181" width="5" height="3" fill="#d8b38a"/><text x="83" y="184">Series 2</text>
        <rect x="118" y="181" width="5" height="3" fill="#ecd6bf"/><text x="125" y="184">Series 3</text></g>
      </svg>
    </div>
  </div>
  <div class="page-foot"><span>RECEIVING ENVIRONMENT MONITORING PROGRAM – FIELD RESULTS REPORT</span><span>7</span></div>
</div>

<!-- Page: back cover -->
<div class="page col-r row-4">
  <svg class="cover-art" viewBox="0 0 100 144" preserveAspectRatio="none" aria-hidden="true">
    <defs>
      <linearGradient id="forestC" x1="0" y1="0" x2="0.6" y2="1">
        <stop offset="0" stop-color="#a9b5a4"/><stop offset=".4" stop-color="#4f6b4c"/><stop offset=".75" stop-color="#7e9a77"/><stop offset="1" stop-color="#d8dcd4"/>
      </linearGradient>
      <linearGradient id="baseC" x1="0" y1="0" x2="1" y2="0">
        <stop offset="0" stop-color="#1f7f78"/><stop offset=".6" stop-color="#6fb1a8"/><stop offset="1" stop-color="#d5a04c"/>
      </linearGradient>
    </defs>
    <rect width="100" height="144" fill="url(#forestC)" role="img" aria-label="Project photograph: rainforest with waterfall"/>
    <path d="M0,56 C35,58 70,74 100,90 L100,95 C70,79 35,63 0,60 Z" fill="#d5a04c"/>
    <path d="M0,60 C35,63 70,79 100,95 L100,105 C74,91 40,71 0,64 Z" fill="#1f7f78"/>
    <path d="M0,64 C40,71 74,91 100,105 L100,144 L0,144 Z" fill="#fff"/>
    <path d="M0,137 C35,132 70,140 100,130 L100,144 L0,144 Z" fill="url(#baseC)" opacity=".85"/>
  </svg>
  <ul class="contact">
    <li><svg viewBox="0 0 14 12"><rect x="1" y="2" width="12" height="8" fill="none" stroke="#d5a04c" stroke-width="1"/><path d="M1 2 L7 7 L13 2" fill="none" stroke="#d5a04c" stroke-width="1"/></svg><span>alex@canopyecology.com.au</span></li>
    <li><svg viewBox="0 0 14 12"><rect x="1" y="1" width="12" height="8" fill="none" stroke="#d5a04c" stroke-width="1"/><path d="M5 11 H9" stroke="#d5a04c" stroke-width="1"/></svg><span>www.canopyecology.com.au</span></li>
    <li><svg viewBox="0 0 14 12"><path d="M7 11 C3 6 3 5 3 4.5 A4 4 0 0 1 11 4.5 C11 5 11 6 7 11 Z" fill="none" stroke="#d5a04c" stroke-width="1"/><circle cx="7" cy="4.5" r="1.3" fill="#d5a04c"/></svg><span>Queensland Office<br>P.O. Box 12<br>Brisbane QLD 4810<br>P: 07 0000 0000<br><br>ABN 00 000 000 000</span></li>
  </ul>
  <div class="cover-logo"><div class="brand lg"><span class="dot"></span>Canopy Ecology</div></div>
</div>

</body>
</html>
```